Brightwell Homes Guide Business card

I have had at the logo designed here and attached. The business compares off the plan apartments in Sydney and provides quick comparison for new home buyers e.g price, floor plans and location. I would like the complimentary colours used on the business card. I would like it be unique but also look professional. I also have a website to gain inspiration from www.brightwellhomesguide.com.au
Updates
Industry/Entity Type
Business
Contact Information for Business Card
Helen Vostrakis
Director of Business Development
e: helen.vostrakis@brightwellhomesguide.com.au
p: (02) 8143 7692
m: 0431 572 908
w: www.brightwellhomesguide.com.au
Look and feel
Each slider illustrates characteristics of the customer's brand and the style your logo design should communicate.

```html
<!DOCTYPE html>
<html lang="en">
<head>
<meta charset="utf-8">
<title>Brightwell Homes Guide – Business Card</title>
<link rel="stylesheet" href="https://fonts.googleapis.com/css2?family=Open+Sans:wght@400;600;700&display=swap">
<style>
  :root {
    --backdrop: #8f9093;
    --card-black: #000000;
    --brand-green: #84c43c;
    --brand-blue: #1396dc;
    --brand-orange: #ff5a1f;
    --text-white: #ffffff;
  }
  * { box-sizing: border-box; margin: 0; padding: 0; }
  html, body {
    width: 1200px;
    height: 900px;
    overflow: hidden;
  }
  body {
    background: var(--backdrop);
    font-family: "Open Sans", sans-serif;
    display: flex;
    flex-direction: column;
    align-items: center;
    justify-content: center;
    gap: 50px;
  }
  .card {
    position: relative;
    width: 560px;
    height: 320px;
    overflow: hidden;
    box-shadow: 0 6px 18px rgba(0,0,0,0.25);
  }
  .card--front {
    background: var(--card-black);
    display: flex;
    align-items: center;
    justify-content: center;
  }
  .brand {
    display: flex;
    align-items: center;
    gap: 12px;
  }
  .brand__square {
    width: 14px;
    height: 14px;
    background: var(--brand-orange);
  }
  .brand__name {
    color: var(--brand-green);
    font-weight: 600;
    font-size: 34px;
    letter-spacing: 0.2px;
  }
  .card--back { background: var(--brand-green); }
  .card__shape {
    position: absolute;
    inset: 0;
    width: 100%;
    height: 100%;
  }
  .card__brand {
    position: absolute;
    left: 36px;
    top: 140px;
    width: 180px;
    display: flex;
    align-items: center;
    gap: 8px;
  }
  .card__brand .brand__square { width: 10px; height: 10px; flex: none; }
  .card__brand .brand__name { font-size: 18px; line-height: 1.2; }
  .contact {
    position: absolute;
    right: 26px;
    top: 38px;
    text-align: right;
    color: var(--text-white);
  }
  .contact__name {
    font-weight: 700;
    font-size: 18px;
    line-height: 1.2;
  }
  .contact__title {
    font-size: 12.5px;
    margin-bottom: 20px;
  }
  .contact__list { list-style: none; }
  .contact__item {
    display: flex;
    justify-content: flex-end;
    align-items: center;
    gap: 9px;
    font-size: 12.5px;
    line-height: 19px;
    white-space: nowrap;
  }
  .contact__item--gap { margin-top: 10px; }
  .contact__icon {
    width: 11px;
    height: 11px;
    flex: none;
    fill: var(--text-white);
  }
  .contact__icon--none { visibility: hidden; }
</style>
</head>
<body>

  <section class="card card--front" aria-label="Business card front">
    <div class="brand">
      <span class="brand__square"></span>
      <span class="brand__name">Brightwell Homes Guide</span>
    </div>
  </section>

  <section class="card card--back" aria-label="Business card back">
    <svg class="card__shape" viewBox="0 0 560 320" preserveAspectRatio="none" aria-hidden="true">
      <path d="M0 0 H246 C300 70 318 200 212 320 H0 Z" fill="var(--brand-blue)"/>
      <path d="M0 0 H232 C288 74 298 206 194 320 H0 Z" fill="var(--card-black)"/>
    </svg>

    <div class="card__brand">
      <span class="brand__square"></span>
      <span class="brand__name">Brightwell Homes Guide</span>
    </div>

    <div class="contact">
      <p class="contact__name">Helen Vostrakis</p>
      <p class="contact__title">Director of Business Development</p>
      <ul class="contact__list">
        <li class="contact__item">(02) 8143 7692
          <svg class="contact__icon" viewBox="0 0 12 12"><path d="M1 4 C1 2 3 1.5 6 1.5 S11 2 11 4 L8.5 4.5 L8 3.5 H4 L3.5 4.5 Z M2.5 6 H9.5 L10.5 10.5 H1.5 Z"/></svg>
        </li>
        <li class="contact__item">0431 572 908
          <svg class="contact__icon" viewBox="0 0 12 12"><path d="M3 0.5 H9 V11.5 H3 Z M4 1.8 V9 H8 V1.8 Z M5.5 9.8 H6.5 V10.6 H5.5 Z"/></svg>
        </li>
        <li class="contact__item">helen.vostrakis
          <svg class="contact__icon" viewBox="0 0 12 12"><path d="M0.5 2.5 H11.5 V9.5 H0.5 Z M1.5 3.5 L6 6.8 L10.5 3.5 Z"/></svg>
        </li>
        <li class="contact__item">@brightwellhomesguide.com.au
          <svg class="contact__icon contact__icon--none" viewBox="0 0 12 12"></svg>
        </li>
        <li class="contact__item">www.brightwellhomesguide.com.au
          <svg class="contact__icon" viewBox="0 0 12 12"><path d="M4.5 6.5 L7.5 3.5 L8.3 4.3 L5.3 7.3 Z M2 8 L4 6 L4.8 6.8 L2.8 8.8 A1.4 1.4 0 0 0 3.2 9.2 L5.2 7.2 L6 8 L4 10 A2.4 2.4 0 0 1 2 8 Z M10 4 L8 6 L7.2 5.2 L9.2 3.2 A1.4 1.4 0 0 0 8.8 2.8 L6.8 4.8 L6 4 L8 2 A2.4 2.4 0 0 1 10 4 Z"/></svg>
        </li>
        <li class="contact__item contact__item--gap">1234, Address Goes Here
          <svg class="contact__icon" viewBox="0 0 12 12"><path d="M6 0.5 A4 4 0 0 1 10 4.5 C10 7.5 6 11.5 6 11.5 C6 11.5 2 7.5 2 4.5 A4 4 0 0 1 6 0.5 Z M6 3 A1.5 1.5 0 1 0 6 6 A1.5 1.5 0 1 0 6 3 Z" fill-rule="evenodd"/></svg>
        </li>
        <li class="contact__item">Sydney NSW, 2000
          <svg class="contact__icon contact__icon--none" viewBox="0 0 12 12"></svg>
        </li>
      </ul>
    </div>
  </section>

</body>
</html>
```